Qorvane Management LLC Business Card

The sample logo was attached for the business Card Design for Traffic Control Company named Qorvane Management LLC. Card design needs to have the company logo and colors match the logo color. It will be nice to show some images of Traffic control signs or cones, even roads closer that math the company services

Target Market(s)

Temporary traffic control. Road closer.

Industry/Entity Type

Construction

Contact Information for Business Card

basic information, name, job title, address, email phone, website

Font styles to use
Serif
Sans Serif

Colors
F0912C
F2A743
F7CA91
FBE8D2
FDF5EE
EE7325
F08F49
F5BC92
FAE3D3
FDF4ED

```html
<!DOCTYPE html>
<html lang="en">
<head>
<meta charset="utf-8">
<title>Qorvane Management LLC Business Card</title>
<link rel="stylesheet" href="https://fonts.googleapis.com/css2?family=Montserrat:wght@500;600;700&family=Open+Sans:wght@400;600&display=swap">
<style>
  :root {
    --orange: #ee7325;
    --orange-deep: #d9632c;
    --charcoal: #3f3f3f;
    --paper: #f6f6f6;
    --paper-shade: #e6e6e6;
    --backdrop: #2a2a2a;
    --ink: #3a3a3a;
  }
  * { margin: 0; padding: 0; box-sizing: border-box; }
  html, body { width: 1200px; height: 900px; overflow: hidden; }
  body { background: var(--backdrop); position: relative; font-family: "Open Sans", sans-serif; }

  .card {
    position: absolute;
    width: 560px;
    height: 320px;
    overflow: hidden;
    box-shadow: 0 14px 30px rgba(0,0,0,.45);
  }
  .card-front { left: 70px; top: 90px; }
  .card-back { left: 570px; top: 490px; }
  .card-art { position: absolute; inset: 0; width: 100%; height: 100%; }

  .wordmark {
    position: absolute;
    display: flex;
    align-items: center;
    gap: 14px;
  }
  .wordmark-dot {
    width: 26px; height: 26px; border-radius: 50%;
    background: var(--orange);
    flex: none;
  }
  .wordmark-name {
    font-family: "Montserrat", sans-serif;
    font-weight: 600;
    color: var(--ink);
    text-transform: uppercase;
    letter-spacing: 2px;
    line-height: 1.15;
  }
  .card-front .wordmark { left: 70px; top: 118px; }
  .card-front .wordmark-name { font-size: 27px; }

  .holder {
    position: absolute;
    left: 34px; top: 150px;
    color: #fff;
  }
  .holder-title { font-size: 15px; font-weight: 400; color: #fbe8d2; }
  .holder-name {
    font-family: "Montserrat", sans-serif;
    font-weight: 700;
    font-size: 20px;
    letter-spacing: .5px;
    color: var(--charcoal);
  }

  .contact-list {
    position: absolute;
    left: 292px; top: 40px;
    list-style: none;
    font-size: 11.5px;
    color: var(--ink);
  }
  .contact-list li { display: flex; align-items: flex-start; gap: 8px; margin-bottom: 6px; line-height: 1.3; }
  .contact-icon { width: 12px; height: 12px; flex: none; margin-top: 2px; fill: var(--orange); }

  .divider {
    position: absolute;
    left: 292px; top: 160px;
    width: 250px; height: 2px;
    background: var(--orange);
  }
  .card-back .wordmark { left: 300px; top: 190px; gap: 10px; }
  .card-back .wordmark-dot { width: 18px; height: 18px; }
  .card-back .wordmark-name { font-size: 17px; letter-spacing: 1.5px; }
</style>
</head>
<body>

<section class="card card-front" aria-label="Card front">
  <svg class="card-art" viewBox="0 0 560 320" preserveAspectRatio="none" aria-hidden="true">
    <defs>
      <linearGradient id="paperFront" x1="0" y1="0" x2="1" y2="1">
        <stop offset="0" stop-color="#fafafa"/>
        <stop offset="1" stop-color="#e4e4e4"/>
      </linearGradient>
    </defs>
    <rect width="560" height="320" fill="var(--orange)"/>
    <path d="M360 55 C455 110 500 220 470 320 L320 320 C395 275 440 195 420 120 Z" fill="var(--charcoal)"/>
    <path d="M0 60 L210 38 C320 30 400 65 420 120 C440 195 395 275 320 320 L0 320 Z" fill="url(#paperFront)"/>
    <path d="M150 48 C260 28 350 40 395 70 C340 48 260 40 150 48 Z" fill="var(--charcoal)"/>
    <path d="M120 58 C220 44 300 46 335 58 C280 52 210 52 120 58 Z" fill="var(--orange)"/>
  </svg>
  <div class="wordmark">
    <span class="wordmark-dot"></span>
    <span class="wordmark-name">Qorvane<br>Management LLC</span>
  </div>
</section>

<section class="card card-back" aria-label="Card back">
  <svg class="card-art" viewBox="0 0 560 320" preserveAspectRatio="none" aria-hidden="true">
    <defs>
      <linearGradient id="paperBack" x1="0" y1="0" x2="1" y2="1">
        <stop offset="0" stop-color="#e8e8e8"/>
        <stop offset="1" stop-color="#fafafa"/>
      </linearGradient>
    </defs>
    <rect width="560" height="320" fill="var(--orange-deep)"/>
    <path d="M252 130 C256 230 340 300 470 320 L310 320 C272 262 248 200 252 130 Z" fill="var(--charcoal)"/>
    <path d="M300 0 L560 0 L560 320 L470 320 C340 300 256 230 252 130 C250 70 270 25 300 0 Z" fill="url(#paperBack)"/>
    <path d="M262 40 C275 20 290 8 305 0 L312 0 C292 14 276 30 262 60 Z" fill="var(--charcoal)"/>
    <path d="M262 110 C264 70 282 30 320 0 L328 0 C292 32 272 70 262 110 Z" fill="var(--orange)"/>
  </svg>

  <div class="holder">
    <p class="holder-title">Director</p>
    <p class="holder-name">DANIEL REYES</p>
  </div>

  <ul class="contact-list">
    <li>
      <svg class="contact-icon" viewBox="0 0 12 12" aria-hidden="true"><path d="M2.5 1 L4.5 1 L5.2 3.5 L4 4.5 C4.6 6 6 7.4 7.5 8 L8.5 6.8 L11 7.5 L11 9.5 C11 10.3 10.3 11 9.5 11 C5 11 1 7 1 2.5 C1 1.7 1.7 1 2.5 1 Z"/></svg>
      <span>(00) 0000 0000</span>
    </li>
    <li>
      <svg class="contact-icon" viewBox="0 0 12 12" aria-hidden="true"><circle cx="6" cy="6" r="5" fill="none" stroke="var(--orange)" stroke-width="1.4"/><path d="M1 6 H11 M6 1 C3.5 4 3.5 8 6 11 M6 1 C8.5 4 8.5 8 6 11" fill="none" stroke="var(--orange)" stroke-width="1"/></svg>
      <span>www.qorvanemanagement.com</span>
    </li>
    <li>
      <svg class="contact-icon" viewBox="0 0 12 12" aria-hidden="true"><path d="M1 3 H11 V10 H1 Z"/><path d="M1 3 L6 7 L11 3" fill="none" stroke="#fff" stroke-width="1"/></svg>
      <span>daniel@qorvanemanagement.com</span>
    </li>
    <li>
      <svg class="contact-icon" viewBox="0 0 12 12" aria-hidden="true"><path d="M6 0.5 C3.8 0.5 2.2 2.1 2.2 4.2 C2.2 7 6 11.5 6 11.5 C6 11.5 9.8 7 9.8 4.2 C9.8 2.1 8.2 0.5 6 0.5 Z M6 2.8 A1.4 1.4 0 1 1 6 5.6 A1.4 1.4 0 1 1 6 2.8 Z"/></svg>
      <span>11 dummy city, dummy place<br>P.O Box 0000 Dummy Land</span>
    </li>
  </ul>

  <div class="divider"></div>

  <div class="wordmark">
    <span class="wordmark-dot"></span>
    <span class="wordmark-name">Qorvane<br>Management LLC</span>
  </div>
</section>

</body>
</html>
```